Lumo Voyages
business cards & letterhead
Lumo Voyages -
Creative Brief
Bright & Fun-filled
Corinne Maddox
58214 Birchwood Ln Rockville, MD 20817
lumovoyages@quellnet.example

```html
<!DOCTYPE html>
<html lang="en">
<head>
<meta charset="utf-8">
<title>Lumo Voyages — Business Card</title>
<link rel="stylesheet" href="https://fonts.googleapis.com/css2?family=Open+Sans:wght@400;600&display=swap">
<style>
  :root {
    --backdrop: #2b2b2d;
    --card: #ffffff;
    --card-shade: #eef0f2;
    --lime: #8cc63f;
    --lime-light: #c5e17a;
    --ocean: #1b75bc;
    --ocean-light: #5fb4e5;
    --ink: #1e1e1e;
    --brand: #2a8fcb;
    --rule: #5a6d86;
  }
  * { margin: 0; padding: 0; box-sizing: border-box; }
  html, body { width: 1200px; height: 751px; overflow: hidden; background: var(--backdrop); }
  body { font-family: "Open Sans", Arial, sans-serif; color: var(--ink); }

  .card {
    position: absolute;
    left: 84px; top: 72px;
    width: 1032px; height: 612px;
    border-radius: 30px;
    overflow: hidden;
    background: linear-gradient(180deg, var(--card) 0%, var(--card) 70%, var(--card-shade) 100%);
  }
  .card-swoosh { position: absolute; inset: 0; width: 100%; height: 100%; }

  .brand {
    position: absolute;
    left: 300px; top: 150px;
    display: flex; align-items: center; gap: 18px;
  }
  .brand-dot {
    width: 70px; height: 70px; border-radius: 50%;
    background: var(--brand);
  }
  .brand-name {
    font-size: 56px; font-weight: 600; letter-spacing: 1px;
    color: var(--brand);
  }

  .holder {
    position: absolute;
    left: 0; top: 362px; width: 465px;
    text-align: right;
    font-size: 34px; font-weight: 400;
  }
  .divider {
    position: absolute;
    left: 485px; top: 365px;
    width: 2px; height: 210px;
    background: var(--rule);
  }
  .contact {
    position: absolute;
    left: 505px; top: 368px;
    font-size: 22px; line-height: 31px;
  }
  .contact-line { display: flex; align-items: center; gap: 14px; }
  .contact-gap { height: 12px; }
  .contact-icon { width: 18px; height: 18px; flex: none; }
</style>
</head>
<body>
  <section class="card" aria-label="Lumo Voyages business card">
    <svg class="card-swoosh" viewBox="0 0 1032 612" preserveAspectRatio="none" aria-hidden="true">
      <path d="M0 250 Q 520 330 1032 200 L1032 212 Q 520 350 0 262 Z" fill="var(--lime)"/>
      <path d="M0 238 Q 520 300 1032 190 L1032 200 Q 520 330 0 250 Z" fill="var(--lime-light)"/>
      <path d="M0 580 Q 516 555 1032 575 L1032 612 L0 612 Z" fill="var(--ocean)"/>
      <path d="M0 572 Q 516 545 1032 566 L1032 578 Q 516 556 0 582 Z" fill="var(--ocean-light)"/>
    </svg>

    <div class="brand">
      <span class="brand-dot"></span>
      <span class="brand-name">Lumo Voyages</span>
    </div>

    <p class="holder">Corinne Maddox</p>
    <div class="divider"></div>

    <div class="contact">
      <p>58214 Birchwood Ln</p>
      <p>Rockville, MD 20817</p>
      <div class="contact-gap"></div>
      <p class="contact-line">
        <svg class="contact-icon" viewBox="0 0 24 24" aria-hidden="true"><path d="M6.6 10.8a15 15 0 0 0 6.6 6.6l2.2-2.2a1 1 0 0 1 1-.25 11.4 11.4 0 0 0 3.6.57 1 1 0 0 1 1 1V20a1 1 0 0 1-1 1A17 17 0 0 1 3 4a1 1 0 0 1 1-1h3.5a1 1 0 0 1 1 1c0 1.25.2 2.45.57 3.57a1 1 0 0 1-.25 1z" fill="var(--ink)"/></svg>
        301-555-0194
      </p>
      <p class="contact-line">
        <svg class="contact-icon" viewBox="0 0 24 24" aria-hidden="true"><rect x="3" y="5" width="18" height="14" rx="1" fill="var(--ink)"/><path d="M3 6l9 7 9-7" stroke="#fff" stroke-width="1.6" fill="none"/></svg>
        lumovoyages@quellnet.example
      </p>
    </div>
  </section>
</body>
</html>
```